Updated website design needed for Radiology Group, Pinebrook Valley Imaging Partners

Clean, uncluttered, updated design needed for top regional Radiology Center. Focus on personal, patient oriented design, (not clinical). Should be simple and easy to navigate, with clear CTAs. Use blues, greens and photos of people in the Central Oregon outdoors.
Uncoded, PSD design only. 2 pages: Home page and one example interior page.
reference current site: http://www.pvipgroup.example/
Sites they like:
http://www.harborscanclinic.example/
http://www.mtqe.example/handler.cfm?event=practice,main
http://www.lindenbonecare.example/

Industry/Entity Type

Medical Imaging

Number of Pages Required

2 page

Font styles to use
Sans Serif

Requirements
Must have
• Personal and patient friendly.
• Lots of white space, clean and uncluttered. Clear CTAs, such as: Patient Bill Pay, Make an Appointment, Meet Our Doctors
• Use copy and contact information from the current site.
• Use outdoor images from Central Oregon, late Winter/ Spring (snow, light colors, spring green, for example)
• Include one example interior page, either Your Exam or Meet Our Doctors
Nice to have
• The client likes:
• Meet Our Doctors slider section, and big, easy to navigate Information Center on www.lindenbonecare.example
• The personal feel of the Your Exam section on www.harborscanclinic.example
• Blues and Greens, outdoorsy imagery
Should not have
• The client does not like:
• complex drop down menus
• clinical feel
• Do not use lorum ipsum or dummy text.
• Do not use outdoor images from other regions. Do not use Summer (hot, poolside) or Fall (red/orange leaves) images.

```html
<!DOCTYPE html>
<html lang="en">
<head>
<meta charset="utf-8">
<title>Pinebrook Valley Imaging Partners</title>
<link rel="stylesheet" href="https://fonts.googleapis.com/css2?family=Montserrat:wght@600;700&family=Open+Sans:wght@400;600;700&family=Raleway:wght@500;600&display=swap">
<style>
:root{
  --navy:#0c2a5f;
  --navy-deep:#082250;
  --nav:#103a78;
  --nav-active:#2c5c9e;
  --title:#1a69a6;
  --text:#6b6f75;
  --text-dark:#3b3f45;
  --rule:#d5d9df;
  --footer-bg:#f1f3f6;
  --white:#ffffff;
}
*{box-sizing:border-box;margin:0;padding:0}
html,body{width:1200px;height:2550px;overflow:hidden;background:var(--white)}
body{font-family:"Open Sans",Arial,sans-serif;color:var(--text);position:relative}
a{color:inherit;text-decoration:none}
.site-header{position:absolute;left:0;top:0;width:1200px;height:107px}
.brand{position:absolute;left:46px;top:16px;display:flex;align-items:center;gap:12px}
.brand-mark{width:76px;height:76px;background:var(--navy)}
.brand-name{font-family:"Open Sans",Arial,sans-serif;font-weight:600;font-size:19px;line-height:24px;color:var(--navy);width:200px}
.contact-box{position:absolute;top:24px;height:58px;background:var(--navy);color:var(--white);text-align:center;padding-top:6px}
.contact-box strong{display:block;font-size:19px;font-weight:600;line-height:24px}
.contact-box span{display:flex;justify-content:center;align-items:center;gap:5px;font-size:13px}
.main-nav{position:absolute;left:0;top:107px;width:1200px;height:63px;background:linear-gradient(#14407f,#0b2d66);display:flex;align-items:center;padding-left:46px}
.main-nav a{color:var(--white);font-size:14px;height:63px;display:flex;align-items:center;padding:0 17px;position:relative}
.main-nav a + a::before{content:"";position:absolute;left:0;top:26px;height:13px;border-left:1px solid rgba(255,255,255,.6)}
.main-nav a.active{background:var(--nav-active);padding:0 20px}
.hero{position:absolute;left:0;top:170px;width:1200px;height:564px}
.hero-photo{position:absolute;inset:0;background:linear-gradient(180deg,#a8d3ef 0%,#c9e3f2 45%,#b9c7b4 70%,#7f935f 100%)}
.hero-panel{position:absolute;left:476px;top:114px;width:724px;height:330px;background:rgba(18,52,104,.82);padding:28px 32px}
.hero-panel h1{font-family:"Montserrat",Arial,sans-serif;font-weight:600;font-size:45px;line-height:54px;color:var(--white);letter-spacing:1px}
.hero-panel p{margin-top:22px;color:var(--white);font-size:14.5px;line-height:23px;text-align:right}
.hero-dots{position:absolute;left:40px;top:286px;display:flex;gap:10px}
.hero-dots i{width:15px;height:15px;border:2px solid var(--white);border-radius:50%}
.hero-dots i.on{background:var(--white)}
.btn{display:inline-block;background:var(--navy);color:var(--white);font-size:12px;font-weight:600}
.hero-panel .btn{position:absolute;right:42px;top:250px;width:128px;height:44px;line-height:44px;text-align:center}
.quick-band{position:absolute;left:0;top:734px;width:1200px;height:138px;background:var(--navy);display:flex}
.quick-item{flex:1;position:relative;text-align:center;color:var(--white);font-weight:700;font-size:17px;line-height:21px;padding-top:56px}
.quick-item + .quick-item{border-left:1px solid rgba(255,255,255,.12)}
.quick-icon{position:absolute;left:50%;top:-44px;margin-left:-44px;width:88px;height:88px;border-radius:50%;background:var(--white);border:3px solid var(--navy);box-shadow:0 0 0 2px var(--white);display:flex;align-items:center;justify-content:center}
.welcome{position:absolute;left:0;top:872px;width:1200px;height:338px;text-align:center;padding:34px 120px 0}
.section-title{font-family:"Raleway",Arial,sans-serif;font-weight:500;font-size:30px;color:var(--title)}
.welcome p{font-size:12px;line-height:21px;margin-top:16px}
.welcome p + p{margin-top:12px}
.welcome .btn{margin-top:26px;width:120px;height:38px;line-height:38px;font-size:11px}
.services{position:absolute;left:0;top:1210px;width:1200px;height:614px}
.services-bg{position:absolute;inset:0;background:linear-gradient(90deg,#dfe1e4 0%,#eceef0 40%,#e9e6ea 70%,#d9d4db 100%)}
.services .section-title{position:absolute;top:34px;left:0;width:1200px;text-align:center;font-size:28px}
.service{position:absolute;width:360px}
.service h3{font-family:"Open Sans",Arial,sans-serif;font-weight:400;font-size:21px;color:var(--title)}
.service p{font-size:12px;line-height:20px;color:var(--text-dark);margin-top:6px}
.service .more{display:block;font-size:11px;color:var(--navy);font-weight:600;margin-top:6px}
.service.left{left:74px;text-align:right}
.service.right{left:765px}
.service-photo{position:absolute;width:112px;height:112px;border-radius:50%;border:3px solid var(--navy);box-shadow:0 0 0 4px var(--white)}
.doctors{position:absolute;left:0;top:1824px;width:1200px;height:361px;background:var(--navy)}
.doctors h2{position:absolute;top:36px;left:0;width:1200px;text-align:center;font-family:"Montserrat",Arial,sans-serif;font-weight:600;font-size:32px;color:var(--white)}
.doctors .rule{position:absolute;top:59px;height:1px;background:rgba(255,255,255,.35);width:375px}
.doctor{position:absolute;top:106px;width:240px;text-align:center;color:var(--white);font-size:16px}
.doctor-photo{width:170px;height:170px;margin:0 auto 12px;border-radius:50%;border:4px solid var(--navy-deep);box-shadow:0 0 0 3px #c9d3e2;background:linear-gradient(180deg,#c5ccd6,#8d97a6)}
.doctor.featured{font-weight:700}
.slider-arrow{position:absolute;top:178px;width:40px;height:40px;border-radius:50%;background:var(--white);display:flex;align-items:center;justify-content:center}
.site-footer{position:absolute;left:0;top:2185px;width:1200px;height:280px;background:var(--footer-bg);display:flex;padding:36px 0 0 53px}
.footer-col{width:290px;padding-right:20px;height:230px}
.footer-col + .footer-col{border-left:1px solid var(--rule);padding-left:28px}
.footer-col h4{font-size:16px;font-weight:600;color:var(--navy);margin-bottom:14px}
.footer-col li{list-style:none;font-size:12px;line-height:28.5px;padding-left:12px;position:relative}
.footer-col li::before{content:"";position:absolute;left:0;top:13px;width:4px;height:4px;border-radius:50%;background:#a5abb3}
.footer-col li b{color:var(--navy);font-weight:600}
.footer-col .more{display:block;font-size:12px;font-weight:700;color:var(--navy);margin-top:4px;padding-left:12px}
.bottom-bar{position:absolute;left:0;top:2465px;width:1200px;height:85px;background:var(--navy);color:var(--white);font-size:12px;padding:49px 46px}
.social{position:absolute;right:34px;top:36px;display:flex;gap:14px}
.social span{width:30px;height:30px;border:1px solid rgba(255,255,255,.8)}
</style>
</head>
<body>

<header class="site-header">
  <div class="brand">
    <div class="brand-mark"></div>
    <div class="brand-name">Pinebrook Valley Imaging Partners</div>
  </div>
  <div class="contact-box" style="left:481px;width:157px"><strong>Medical Records:</strong><span><svg width="11" height="11" viewBox="0 0 24 24"><path fill="#fff" d="M6.6 10.8a15 15 0 006.6 6.6l2.2-2.2c.3-.3.7-.4 1-.2 1.1.4 2.3.6 3.6.6.6 0 1 .4 1 1V20c0 .6-.4 1-1 1A17 17 0 013 4c0-.6.4-1 1-1h3.5c.6 0 1 .4 1 1 0 1.3.2 2.5.6 3.6.1.3 0 .7-.2 1z"/></svg>+ (555) 201-4410</span></div>
  <div class="contact-box" style="left:665px;width:156px"><strong>Billing:</strong><span><svg width="11" height="11" viewBox="0 0 24 24"><path fill="#fff" d="M6.6 10.8a15 15 0 006.6 6.6l2.2-2.2c.3-.3.7-.4 1-.2 1.1.4 2.3.6 3.6.6.6 0 1 .4 1 1V20c0 .6-.4 1-1 1A17 17 0 013 4c0-.6.4-1 1-1h3.5c.6 0 1 .4 1 1 0 1.3.2 2.5.6 3.6.1.3 0 .7-.2 1z"/></svg>+ (555) 201-4422</span></div>
  <div class="contact-box" style="left:847px;width:156px"><strong>Scheduling:</strong><span><svg width="11" height="11" viewBox="0 0 24 24"><path fill="#fff" d="M6.6 10.8a15 15 0 006.6 6.6l2.2-2.2c.3-.3.7-.4 1-.2 1.1.4 2.3.6 3.6.6.6 0 1 .4 1 1V20c0 .6-.4 1-1 1A17 17 0 013 4c0-.6.4-1 1-1h3.5c.6 0 1 .4 1 1 0 1.3.2 2.5.6 3.6.1.3 0 .7-.2 1z"/></svg>+ (555) 201-4437</span></div>
  <div class="contact-box" style="left:1023px;width:131px"><strong>Main Line:</strong><span><svg width="11" height="11" viewBox="0 0 24 24"><path fill="#fff" d="M6.6 10.8a15 15 0 006.6 6.6l2.2-2.2c.3-.3.7-.4 1-.2 1.1.4 2.3.6 3.6.6.6 0 1 .4 1 1V20c0 .6-.4 1-1 1A17 17 0 013 4c0-.6.4-1 1-1h3.5c.6 0 1 .4 1 1 0 1.3.2 2.5.6 3.6.1.3 0 .7-.2 1z"/></svg>+ (555) 201-4400</span></div>
</header>

<nav class="main-nav">
  <a class="active" href="#">Home</a>
  <a href="#">About Us</a>
  <a href="#">Our Service</a>
  <a href="#">For Patients</a>
  <a href="#">Our Physicians</a>
  <a href="#">For Physicians</a>
  <a href="#">PACS &amp; Document</a>
  <a href="#">Appointment</a>
  <a href="#">Our Location</a>
</nav>

<section class="hero">
  <div class="hero-photo" role="img" aria-label="Two cyclists riding mountain bikes on a sunny spring trail under a blue sky"></div>
  <div class="hero-panel">
    <h1>Welcome to Pinebrook Valley Imaging Partners</h1>
    <p>Pinebrook Valley Imaging Partners is a diagnostic imaging corporation providing professional services to Central and Eastern Oregon hospitals and clinics as well as state-of-the-art services in its' own outpatient imaging center.</p>
    <div class="hero-dots"><i></i><i></i><i class="on"></i><i></i><i></i></div>
    <a class="btn" href="#">Read More</a>
  </div>
</section>

<section class="quick-band">
  <a class="quick-item" href="#"><span class="quick-icon"><svg width="36" height="36" viewBox="0 0 24 24" fill="none" stroke="#0c2a5f" stroke-width="1.6"><path d="M6 2h9l4 4v16H6z"/><path d="M15 2v4h4M9 11h7M9 14h7M9 17h5"/></svg></span>Patient Bill<br>Pay</a>
  <a class="quick-item" href="#"><span class="quick-icon"><svg width="36" height="36" viewBox="0 0 24 24" fill="none" stroke="#0c2a5f" stroke-width="2"><circle cx="12" cy="12" r="9"/><path d="M12 7v5l3 2"/></svg></span>Make an<br>Appointment</a>
  <a class="quick-item" href="#"><span class="quick-icon"><svg width="36" height="36" viewBox="0 0 24 24" fill="#0c2a5f"><circle cx="12" cy="7" r="4"/><path d="M4 21c0-5 3.5-8 8-8s8 3 8 8z"/></svg></span>Meet Our<br>Doctors</a>
  <a class="quick-item" href="#"><span class="quick-icon"><svg width="36" height="36" viewBox="0 0 24 24"><path fill="#0c2a5f" d="M12 2a7 7 0 00-7 7c0 5 7 13 7 13s7-8 7-13a7 7 0 00-7-7z"/><circle cx="12" cy="9" r="2.6" fill="#fff"/></svg></span>Find a<br>Location</a>
  <a class="quick-item" href="#"><span class="quick-icon"><svg width="36" height="36" viewBox="0 0 24 24" fill="none" stroke="#0c2a5f" stroke-width="1.6"><path d="M5 22V3h14v19zM3 22h18"/><path d="M8 6h2M14 6h2M8 10h2M14 10h2M8 14h2M14 14h2M10 22v-4h4v4"/></svg></span>Events &amp;<br>Classes</a>
  <a class="quick-item" href="#"><span class="quick-icon"><svg width="36" height="36" viewBox="0 0 24 24" fill="#0c2a5f"><circle cx="12" cy="8" r="5"/><path d="M3 22c0-5 4-8 9-8s9 3 9 8z"/></svg></span>Customer<br>Care</a>
  <a class="quick-item" href="#"><span class="quick-icon"><svg width="36" height="36" viewBox="0 0 24 24" fill="none" stroke="#0c2a5f" stroke-width="1.6"><path d="M3 5h13v9H8l-4 3v-3H3z"/><path d="M16 8h5v9h-1v3l-4-3h-5v-3"/></svg></span>Patient<br>Testimonials</a>
</section>

<section class="welcome">
  <h2 class="section-title">Welcome to Pinebrook Valley Imaging Partners</h2>
  <p>Pinebrook Valley Imaging Partners is a diagnostic imaging corporation providing professional services to Central and Eastern Oregon hospitals and clinics as well as state-of-the-art services in its' own outpatient imaging center. PVIP was established by its' founder, Harold M. Whitcombe, MD when he opened his Central Oregon practice in 1947.</p>
  <p>PVIP is staffed by fellowship trained physicians with expertise in major disciplines to include mammography, ultrasound, Magnetic Resonance Imaging, Computed Tomography, Positron Emission Tomography, interventional procedures, Nuclear Medicine and general procedures which include fluoroscopy, tomography, IVP's and radiographic procedures for head, chest, abdomen and extremity examinations.</p>
  <a class="btn" href="#">READ MORE</a>
</section>

<section class="services">
  <div class="services-bg" role="img" aria-label="Soft faded background of a smiling technician helping a patient"></div>
  <h2 class="section-title">Our Service</h2>
  <svg width="1200" height="614" style="position:absolute;left:0;top:0" aria-hidden="true">
    <g stroke="#b9c2cf" stroke-width="2" fill="none">
      <path d="M500 159v308M692 159v308M500 159h192M500 308h192M500 478h192"/>
    </g>
  </svg>
  <div class="service-photo" style="left:444px;top:103px;background:radial-gradient(#3d7fd0,#0d2a6e)" role="img" aria-label="Illustration of a colon"></div>
  <div class="service-photo" style="left:636px;top:103px;background:linear-gradient(#dfe4ea,#8a96a6)" role="img" aria-label="MRI scanner room"></div>
  <div class="service-photo" style="left:444px;top:252px;background:radial-gradient(#9a9a9a,#151515)" role="img" aria-label="Mammogram image"></div>
  <div class="service-photo" style="left:636px;top:252px;background:linear-gradient(#cfd9e6,#5d7794)" role="img" aria-label="Patient in a CT scanner"></div>
  <div class="service-photo" style="left:444px;top:422px;background:linear-gradient(#e8ecf1,#8ea0b6)" role="img" aria-label="Ultrasound probe in hand"></div>
  <div class="service-photo" style="left:636px;top:422px;background:linear-gradient(#d6dce4,#6c7c90)" role="img" aria-label="X-ray radiography room"></div>

  <div class="service left" style="top:110px"><h3>Virtual Colonoscopy (VC)</h3><p>Virtual Colonoscopy (VC), also referred to as CT colonography,<br>is a safe exam used for colon polyp screening.</p><a class="more" href="#">READ MORE &#9656;</a></div>
  <div class="service left" style="top:260px"><h3>Digital Mammography</h3><p>Advanced level obstetric, abdominal, pelvic and small parts<br>imaging.</p><a class="more" href="#">READ MORE &#9656;</a></div>
  <div class="service left" style="top:420px"><h3>Ultrasound</h3><p>Advanced level obstetric, abdominal, pelvic and small parts<br>imaging.</p><a class="more" href="#">READ MORE &#9656;</a></div>
  <div class="service right" style="top:110px"><h3>Magnetic Resonance Imaging (MRI)</h3><p>PVMRI has three convenient locations Alder Creek (Mill<br>Street), PVIP on the eastside of Pinebrook, and PVMC-North.</p><a class="more" href="#">READ MORE &#9656;</a></div>
  <div class="service right" style="top:260px"><h3>Computed Tomography (CT)</h3><p>PVIP now offers extended CT hours at our eastside location.<br>7:00 am – 6:30 pm.</p><a class="more" href="#">READ MORE &#9656;</a></div>
  <div class="service right" style="top:425px"><h3>General Radiography</h3><p>We welcome patients for emergent and walk-in plain<br>films.</p><a class="more" href="#">READ MORE &#9656;</a></div>
</section>

<section class="doctors">
  <span class="rule" style="left:48px"></span>
  <h2>Meet Our Doctors</h2>
  <span class="rule" style="left:777px"></span>
  <span class="slider-arrow" style="left:24px"><svg width="14" height="14" viewBox="0 0 24 24"><path d="M15 4l-8 8 8 8" stroke="#0c2a5f" stroke-width="3.5" fill="none"/></svg></span>
  <div class="doctor" style="left:50px"><div class="doctor-photo" role="img" aria-label="Portrait of Dr. Owen Marlow"></div>Owen Marlow, M.D.</div>
  <div class="doctor" style="left:330px"><div class="doctor-photo" role="img" aria-label="Portrait of Dr. Dana Hollister-Reyes"></div>Dana Hollister-Reyes, M.D.</div>
  <div class="doctor featured" style="left:623px"><div class="doctor-photo" role="img" aria-label="Portrait of Dr. Evan Stroud"></div>Evan Stroud, M.D.</div>
  <div class="doctor" style="left:907px"><div class="doctor-photo" role="img" aria-label="Portrait of Dr. Evan Stroud"></div>Evan Stroud, M.D.</div>
  <span class="slider-arrow" style="left:1138px"><svg width="14" height="14" viewBox="0 0 24 24"><path d="M9 4l8 8-8 8" stroke="#0c2a5f" stroke-width="3.5" fill="none"/></svg></span>
</section>

<footer class="site-footer">
  <div class="footer-col"><h4>For Patients</h4><ul><li>About Your Visit</li><li>Why Choose Us?</li><li>Patient Forms</li><li>Billing and Insurance</li></ul><a class="more" href="#">More +</a></div>
  <div class="footer-col"><h4>Quick Links</h4><ul><li>About Us</li><li>Our Physicians</li><li>For Physicians</li><li>Disclaimer</li></ul><a class="more" href="#">More +</a></div>
  <div class="footer-col"><h4>Our Services</h4><ul><li>Mammography</li><li>MRI</li><li>CT-64</li><li>X-Ray</li></ul><a class="more" href="#">More +</a></div>
  <div class="footer-col"><h4>Contact Us</h4><ul><li>(555) 201-4400 - <b>Main Line</b></li><li>(555) 201-4437 - <b>Scheduling</b></li><li>(555) 201-4422 - <b>Billing</b></li><li>(555) 201-4410 - <b>Medical Records</b></li></ul></div>
</footer>

<div class="bottom-bar">
  Copyright 2016 Company Name.&nbsp; All Rights Reserved.
  <div class="social" aria-label="Social links"><span></span><span></span><span></span></div>
</div>

</body>
</html>
```